Fernbrook Vale Executive Development Workshop Series

* Had error in first version of MS Word doc and have re-uploaded - twelve subject areas, not nine *
I'd like a flyer to print to hand out and post on my website fernbrookvale.com to advertise a workshop series I'm launching. I'd like it to build strongly on the wonderful logo you did and Scottish theme...and to have the same "feel" as my website. fernbrookvale.com
It should be 8.5x11, single sided. Not sure if I should use full color glossy or two-color on nice paper. Regardless, I will most likely have it done on a color copier and will not put it on a printing press.
I have typed up a document with all the information in a MS Word file, but need you to lay it out in an aesthetically pleasing way. I have attached that MS Word file.
I am also attaching a handful of similar flyer documents from other non-competing coaches in my network. I think they all have their merits, but leave me under-whelmed.
I'm also attaching a picture of me and some pictures of Scotland my parents took about 10 years ago. I'm reluctantly open to stock photos, just not too obvious or hackneyed (if that word can be applied to pictures as well as expressions).
Lastly, this workshop series will be an ongoing thing, so I'd like to be able to make minor edits myself with things like new dates or topics.
Thank you!
Target Market(s)
Small business owners and emerging leaders with large companies
Colors
Designer to choose colors to be used in the design.
Requirements
Should not have
- Obviously stock photos

```html
<!DOCTYPE html>
<html lang="en">
<head>
<meta charset="utf-8">
<title>Fernbrook Vale Executive Development Workshop Series</title>
<link href="https://fonts.googleapis.com/css2?family=Tinos:wght@400;700&family=Mulish:wght@400;500;600;700&display=swap" rel="stylesheet">
<style>
  :root{
    --olive-dark:#3c4124;
    --olive:#4b5322;
    --sage:#b8cb93;
    --ink:#3b3b30;
    --muted:#55554a;
    --white:#ffffff;
    --page-bg:#e9e9e6;
    --seal:#c9ccc0;
  }
  *{margin:0;padding:0;box-sizing:border-box}
  html,body{width:1016px;height:1200px;overflow:hidden;background:var(--page-bg)}
  .sheet-wrap{position:absolute;left:44px;top:0;width:927px;height:1200px}
  .sheet{position:absolute;left:0;top:0;width:850px;height:1100px;background:var(--white);
    transform:scale(1.0909);transform-origin:0 0;font-family:"Mulish",sans-serif;color:var(--ink);overflow:hidden}
  .abs{position:absolute}
  .hero-art{position:absolute;left:0;top:0}
  .series-title{left:0;top:20px;width:850px;text-align:center;font-family:"Tinos",serif;font-size:23px;font-weight:400;color:var(--white)}
  .series-title b{font-weight:700}
  .coach-name{left:38px;top:128px;font-family:"Tinos",serif;font-size:40px;color:var(--white);font-weight:400}
  .name-rule{left:38px;top:176px;width:358px;height:1px;background:var(--sage)}
  .coach-role{left:38px;top:184px;font-size:17px;color:#e6e6dc}
  .tagline{left:38px;top:234px;width:506px;font-size:17px;line-height:21.5px;color:var(--white);text-align:justify}
  .intro{left:24px;top:403px;width:358px;font-size:12.8px;line-height:16.6px;color:var(--muted);text-align:justify}
  .intro p+p{margin-top:17px}
  .rule{height:1px;background:var(--sage)}
  .includes-title{left:25px;top:578px;font-size:16.5px;font-weight:600;color:var(--olive-dark)}
  .includes{left:25px;top:610px;width:367px;list-style:none}
  .includes li{position:relative;padding-left:21px;margin-bottom:8px}
  .includes .dot{position:absolute;left:0;top:3px;width:13px;height:13px;border-radius:50%;background:var(--sage)}
  .includes .dot::after{content:"";position:absolute;left:4px;top:3.5px;width:3px;height:3px;border-right:1.5px solid #fff;border-bottom:1.5px solid #fff;transform:rotate(-45deg)}
  .includes h3{font-size:13px;font-weight:500;color:var(--olive-dark)}
  .includes p{font-size:13px;line-height:16.6px;color:var(--muted);text-align:justify}
  .fine{left:33px;top:790px;width:351px;font-size:11.2px;line-height:14px;color:var(--muted);text-align:justify}
  .venue{left:33px;top:862px;width:351px;font-size:11.6px;line-height:14px;color:var(--olive-dark);text-align:justify}
  .price{left:33px;top:922px;width:360px;font-size:16px;line-height:20.5px;font-weight:600;color:var(--olive-dark)}
  .topics{left:432px;top:452px;width:390px;list-style:none}
  .topics li{position:relative;padding-left:14px;margin-bottom:3.5px}
  .topics li::before{content:"›";position:absolute;left:0;top:-4px;font-size:17px;font-weight:700;color:var(--olive-dark)}
  .topics h4{font-size:14px;font-weight:500;color:var(--olive-dark);line-height:16px}
  .topics h4 b{font-weight:700}
  .topics p{font-size:12.6px;line-height:14.6px;color:var(--ink)}
  .member-seal{left:780px;top:452px;width:42px;height:42px;border-radius:50%;background:var(--seal)}
  .register{left:424px;top:928px;width:399px;height:51px;border:1.5px solid var(--olive-dark);
    text-align:center;font-size:16.5px;line-height:19px;padding-top:5px;color:var(--olive-dark)}
  .register b{font-weight:600}
  .footer-line{left:0;top:994px;width:850px;height:8px;background:var(--sage)}
  .footer{left:0;top:1002px;width:850px;height:98px;background:var(--olive-dark);color:var(--white)}
  .footer-name{left:31px;top:14px;font-family:"Tinos",serif;font-size:14px}
  .footer-name b{font-weight:700}
  .contacts{left:31px;top:36px;list-style:none;font-size:12px;line-height:17px;color:#e4e4d8}
  .contacts li{display:flex;align-items:center;gap:7px}
  .contacts svg{width:10px;height:10px;fill:#cfcfc2}
  .brand{right:30px;top:30px;display:flex;align-items:center;gap:10px;font-size:24px;font-weight:600;color:var(--white)}
  .brand .mark{width:14px;height:14px;border-radius:50%;background:var(--sage)}
</style>
</head>
<body>
<div class="sheet-wrap">
<main class="sheet">
  <svg class="hero-art" width="850" height="445" viewBox="0 0 850 445">
    <defs>
      <linearGradient id="landscape" x1="0" y1="0" x2="0" y2="1">
        <stop offset="0" stop-color="#e3e4e0"/>
        <stop offset="0.25" stop-color="#a9ab9e"/>
        <stop offset="0.45" stop-color="#6a6b4c"/>
        <stop offset="0.7" stop-color="#7b6a3c"/>
        <stop offset="1" stop-color="#5c4a2c"/>
      </linearGradient>
      <radialGradient id="portrait" cx="0.5" cy="0.45" r="0.6">
        <stop offset="0" stop-color="#d7c2b2"/>
        <stop offset="1" stop-color="#8a7b6a"/>
      </radialGradient>
    </defs>
    <rect x="0" y="55" width="850" height="380" fill="url(#landscape)" role="img" aria-label="Photograph of Scottish highland glen with misty mountains and heather moorland"/>
    <path d="M0 0 H850 V60 Q425 120 0 56 Z" fill="#3c4124"/>
    <path d="M0 56 Q425 120 850 60 V78 Q425 118 0 80 Z" fill="#ffffff"/>
    <path d="M0 322 C230 380 520 402 850 396 V445 H0 Z" fill="#b8cb93"/>
    <path d="M0 330 C240 395 520 432 850 432 V445 H0 Z" fill="#ffffff"/>
    <circle cx="738" cy="248" r="88" fill="#b4b8a0" opacity="0.85"/>
    <circle cx="738" cy="248" r="79" fill="url(#portrait)" role="img" aria-label="Portrait photograph of the coach"/>
  </svg>

  <h1 class="abs series-title">Fernbrook Vale Executive Development Workshop Series – <b>First Thursdays</b></h1>
  <h2 class="abs coach-name">Graham Keller</h2>
  <div class="abs name-rule"></div>
  <p class="abs coach-role">Certified Professional Business Coach</p>
  <p class="abs tagline">A positive, fresh, results-driven approach for businesses to increase profits by building confidence, command and control in owners and executives.</p>

  <section class="abs intro">
    <p>We will use proven leadership and business strategies to improve work-life balance, buy-in, and company value. Here’s your opportunity to meet with other like-minded business owners and executives once a month in a private and confidential setting.</p>
    <p>We’ve got nine subject areas planned, and while they are all powerful, we will shift from high-level strategy topics to “where the rubber meets the road” topics.</p>
  </section>

  <div class="abs rule" style="left:24px;top:567px;width:370px"></div>
  <h2 class="abs includes-title">Monthly Workshop Series Includes:</h2>
  <ul class="abs includes">
    <li><span class="dot"></span><h3>3-Hour Intensive Workshop</h3>
      <p>High-energy, creative sessions with engaging and relevant business topics, peer group advisory board (master mind), and networking (9am – 12pm, dates above)</p></li>
    <li><span class="dot"></span><h3>90-minute one-on-one coaching session</h3>
      <p>to help you absorb and apply the revelations from the group sessions to your own business (mutually scheduled)</p></li>
  </ul>
  <div class="abs rule" style="left:24px;top:779px;width:370px"></div>

  <p class="abs fine">Participation and trust is vital to your investment; no holding back. Due to the confidential nature of the intensive workshops, all participants will sign a confidentiality agreement. Additionally, we will only allow one company per industry to be represented.</p>
  <p class="abs venue">All monthly Intensive Workshops will be 9am – 12pm on the dates at Millrace Coworking at 212 Foundry Lane, Riverton NC 27000</p>
  <p class="abs price">$395/month or $295/month with a 6-month or greater commitment</p>

  <ul class="abs topics">
    <li><h4><b>SEP 7</b> – My Company Owns Me</h4><p>What a CEO should and should not do</p></li>
    <li><h4><b>OCT 5</b> – Taking Vision / Mission / Values</h4><p>Down To The Molecular Level Of Your Company</p></li>
    <li><h4><b>NOV 2</b> – People Problems</h4><p>The biggest waste of time and money for every small business</p></li>
    <li><h4><b>Dec 7</b> – Value Delivery Systems</h4><p>Re-think everything you think you know about creating value</p></li>
    <li><h4><b>Jan 4, 2018</b> – Rally Your Team Around A Goal</h4><p>How to create a meaningful company goal and rally the troops around it</p></li>
    <li><h4><b>Feb 1</b> – Building Your Executive Leadership Team</h4><p>You can’t succeed without one</p></li>
    <li><h4><b>Mar 1</b> – Improve Your Outside Sales Efforts</h4><p>Help your sales force to be busy AND successful</p></li>
    <li><h4><b>Apr 5</b> – Every Brain In The Game</h4><p>Engage your team and build a strong culture</p></li>
    <li><h4><b>May 3</b> – Repeatable Processes</h4><p>Coach your employees how to get predictable results every time</p></li>
    <li><h4><b>Jun 7</b> – Finding and Filling Profit Holes</h4><p>Most small businesses waste more money than they profit</p></li>
    <li><h4><b>Jul 12</b> – Put Your Payroll On A Diet</h4><p>Why waste happens, what to do about it and how it helps everyone</p></li>
    <li><h4><b>Aug 2</b> – Truly, How Effective Are You With This Whole “Leadership” Thing?</h4></li>
  </ul>

  <div class="abs member-seal" role="img" aria-label="Professional association membership badge"></div>

  <p class="abs register">To register, go to <b>fernbrookvale.com/exec-dev</b> and click the registration link</p>

  <div class="abs footer-line"></div>
  <footer class="abs footer">
    <p class="abs footer-name"><b>GRAHAM KELLER,</b> Certified Professional Business Coach</p>
    <ul class="abs contacts">
      <li><svg viewBox="0 0 10 10"><path d="M2 0.5 L3.8 2.6 L2.9 3.8 Q4 6 6.2 7.1 L7.4 6.2 L9.5 8 L8.4 9.5 Q1 8.5 0.5 1.6 Z"/></svg>(555)014-2287</li>
      <li><svg viewBox="0 0 10 10"><path d="M0.5 2 H9.5 V8 H0.5 Z M1 2.5 L5 5.5 L9 2.5" stroke="#3c4124" stroke-width="0.8"/></svg>graham@fernbrookvale.com</li>
      <li><svg viewBox="0 0 10 10"><circle cx="5" cy="5" r="4.5"/><path d="M0.5 5 H9.5 M5 0.5 V9.5" stroke="#3c4124" stroke-width="0.8"/></svg>fernbrookvale.com</li>
    </ul>
    <div class="abs brand"><span class="mark"></span>Fernbrook Vale</div>
  </footer>
</main>
</div>
</body>
</html>
```